CRM Application Interface Design

We have a wireframe / design draft for a CRM application (similar to Quillmarket, Kavu, etc.). We need this draft to be restyled to create a more finished, polished application user interface. There is a specific branding color scheme that must be adhered to, but you may add secondary and tertiary colors as needed.
At a minimum, these branding colors are required to appear in the design:
#CC0000 : Primary brand color
#AA0000 : Primary shaded (e.g. hover) color
#DBEEF5 / #4A4A4A : Gray
Some other colors you may wish to add:
* "Error/warning" color of your choice
* "Informational / focus" color of your choice
Two screens are provided, both should be re-styled as you see fit in order to finish the design:
1. "Search for customers" screen
2. "View customer details" screen
Requirements:
1. Must have the navigation along the top, cannot switch to a left nav. Must also remain two-level navigation (primary nav at top with sub nav beneath it).
2. The design must use the primary red color in a thoughtful, balanced way, without overdoing it. Please make use of other colors if needed to offset the use of red.
3. Text must be high enough contrast to be readable. The wireframe/draft screens attached show a "washed-out" low-contrast UI with light gray text. That design theme should not be used in the final design.
Aside from the above requirements, please feel free to think creatively and present substantially different ideas. Some of the things we are open to changing include:
* Element style (eg. square vs. rounded corners, flat vs. depth)
* Use of color vs. grayscale
* Menus and navigation
* Light / dark theme
* Any other stylistic elements
* Minor layout changes can be made if needed, but elements should not be moved if that can be avoided.
Goals:
* This is a business application that is used frequently and for long periods, so should not have any unnecessary distracting elements.
* Looking for a design that is clean, professional, readable, usable, and intuitive.

```html
<!DOCTYPE html>
<html lang="en">
<head>
<meta charset="utf-8">
<title>Customers – Search</title>
<link href="https://fonts.googleapis.com/css2?family=Barlow:wght@300;400;500;600;700&display=swap" rel="stylesheet">
<style>
:root{
  --brand:#cc0000;
  --brand-dark:#aa0000;
  --ink:#1a1a1a;
  --gray:#4a4a4a;
  --muted:#8a8a8a;
  --line:#dcdcdc;
  --page:#f4f4f4;
  --row-alt:#f7f7f7;
  --row-selected:#fdf1f1;
  --head:#e9e9e9;
}
*{box-sizing:border-box;margin:0;padding:0}
html,body{width:1149px;height:1200px;overflow:hidden;background:var(--page)}
body{font-family:'Barlow',sans-serif;color:var(--ink)}
.app{width:1366px;height:1427px;transform:scale(.8411);transform-origin:0 0;position:relative;background:var(--page)}

.topbar{height:76px;background:#fff;position:relative}
.brand{position:absolute;left:40px;top:24px;display:flex;align-items:center;gap:10px}
.brand-square{width:24px;height:24px;background:var(--brand)}
.brand-name{font-size:24px;font-weight:700;color:var(--ink);letter-spacing:.5px}
.mainnav{position:absolute;left:234px;top:0;height:76px;display:flex;gap:39px}
.mainnav a{font-size:15px;font-weight:600;color:var(--ink);position:relative;height:76px;line-height:84px}
.mainnav a.active{color:var(--brand)}
.mainnav a.active::after{content:"";position:absolute;left:50%;bottom:0;margin-left:-7px;border:7px solid transparent;border-bottom-color:var(--brand-dark);border-top:0}
.usernav{position:absolute;right:40px;top:18px;display:flex;align-items:center;gap:14px;font-size:13px;font-weight:500}
.usernav span{display:flex;align-items:center;gap:4px}
.avatar{width:40px;height:40px;border-radius:50%;background:linear-gradient(#d8b89a,#a47a5c)}

.subnav{height:36px;background:var(--brand-dark);display:flex;padding-left:234px}
.subnav a{color:#fff;font-size:13px;font-weight:700;padding:0 20px;line-height:36px}
.subnav a.active{background:var(--brand)}

.filterband{height:188px;background:var(--gray);padding:48px 40px 0}
.searchbar{height:52px;background:#fff;display:flex;align-items:center;padding:0 8px 0 16px}
.searchbar h1{font-size:19px;font-weight:700;flex:1}
.searchbar h1 small{font-size:14px;font-weight:500}
.btn{height:36px;border:none;border-radius:4px;background:var(--ink);color:#fff;font-family:inherit;font-size:12px;font-weight:700;padding:0 12px;margin-left:4px;display:flex;align-items:center;gap:5px}
.btn.red{background:var(--brand)}
.chips{display:flex;gap:4px;margin-top:16px}
.chip{height:24px;border:1px solid #fff;border-radius:12px;color:#fff;font-size:11px;font-weight:600;padding:0 11px;display:flex;align-items:center;gap:7px}
.chip b{font-size:13px}

.results{position:absolute;left:40px;top:330px;width:1286px}
.results-head{height:78px;position:relative}
.results-head h2{position:absolute;left:0;top:30px;font-size:31px;font-weight:300}
.filterinput{position:absolute;left:200px;top:30px;width:298px;height:35px;border:1px solid var(--line);border-radius:4px;background:#fff;font-size:12px;font-style:italic;color:#666;padding-left:34px;line-height:33px}
.filterinput svg{position:absolute;left:14px;top:10px}
.tooltip{position:absolute;left:1118px;top:0;width:100px;height:29px;background:var(--gray);color:#fff;font-size:13px;font-weight:500;text-align:center;line-height:31px}
.tooltip::after{content:"";position:absolute;left:44px;bottom:-6px;border:6px solid transparent;border-top-color:var(--gray);border-bottom:0}
.gear{position:absolute;left:1153px;top:36px;width:30px;height:30px;background:var(--brand);border-radius:3px;display:flex;align-items:center;justify-content:center}
.excel{position:absolute;left:1187px;top:36px;width:99px;height:30px;border:1px solid var(--brand);border-radius:3px;background:#fff;color:var(--brand);font-size:12px;font-weight:700;display:flex;align-items:center;justify-content:center;gap:5px}
.tablebox{background:#fff;border:1px solid var(--line);height:979px}
table{width:100%;border-collapse:collapse;font-size:14px}
th{height:35px;background:var(--head);text-align:left;font-size:12px;font-weight:700;border-bottom:1px solid var(--line)}
th .sort{font-weight:400;margin-left:4px}
td{height:48px}
tbody tr:nth-child(even){background:var(--row-alt)}
tbody tr.selected{background:var(--row-selected)}
.c-check{width:42px;padding-left:20px}
.c-star{width:40px;font-size:19px;color:var(--muted)}
tr.selected .c-star{color:var(--ink)}
.c-name{width:240px}.c-office{width:160px}.c-login{width:160px}.c-email{width:383px}.c-phone{width:177px}
.box{width:14px;height:14px;border:1px solid #999;border-radius:2px;background:#fff;display:flex;align-items:center;justify-content:center}
.box.on{background:var(--brand);border-color:var(--brand)}
.action{color:var(--brand);font-size:12px;font-weight:700;display:flex;align-items:center;gap:6px}
.pager{display:flex;justify-content:center;align-items:center;margin-top:24px;font-size:12px;color:var(--gray)}
.pager .count{margin-right:12px}
.pages{display:flex;border:1px solid var(--line)}
.pages span{width:29px;height:29px;line-height:29px;text-align:center;color:var(--brand);font-weight:700;border-right:1px solid var(--line)}
.pages span:last-child{border:none}
.pages span.first{color:var(--ink)}
.pages span.cur{background:#e8e8e8;color:var(--ink)}
</style>
</head>
<body>
<div class="app">
  <header class="topbar">
    <div class="brand"><span class="brand-square"></span><span class="brand-name">MERIDIAN</span></div>
    <nav class="mainnav">
      <a>DASHBOARD</a><a class="active">CUSTOMERS</a><a>ADMIN</a><a>SALES</a><a>SETTINGS</a>
    </nav>
    <div class="usernav">
      <span><svg width="10" height="12" viewBox="0 0 10 12"><path d="M5 0a4 4 0 0 0-4 4c0 3 4 8 4 8s4-5 4-8a4 4 0 0 0-4-4zm0 5.5A1.5 1.5 0 1 1 5 2.5a1.5 1.5 0 0 1 0 3z" fill="#1a1a1a"/></svg>Locations <svg width="12" height="7"><path d="M1 1l5 5 5-5" stroke="#cc0000" fill="none"/></svg></span>
      <span><svg width="12" height="12" viewBox="0 0 12 12"><path d="M6 0l1.8 4 4.2.4-3.2 2.8 1 4.1L6 9.2 2.2 11.3l1-4.1L0 4.4 4.2 4z" fill="#1a1a1a"/></svg>Favorites <svg width="12" height="7"><path d="M1 1l5 5 5-5" stroke="#cc0000" fill="none"/></svg></span>
      <span><span class="avatar" role="img" aria-label="User profile photo"></span><svg width="12" height="7"><path d="M1 1l5 5 5-5" stroke="#cc0000" fill="none"/></svg></span>
    </div>
  </header>
  <nav class="subnav"><a class="active">SEARCH</a><a>LEADS</a><a>PROSPECTS</a><a>COMPANIES</a></nav>

  <section class="filterband">
    <div class="searchbar">
      <h1><small>PEOPLE: </small>Search</h1>
      <button class="btn">MODIFY SEARCH</button>
      <button class="btn">SAVE SEARCH</button>
      <button class="btn">NEW CUSTOMER</button>
      <button class="btn red"><svg width="13" height="10" viewBox="0 0 13 10"><rect width="13" height="10" fill="#fff"/><path d="M0 0l6.5 5L13 0" stroke="#cc0000" fill="none"/></svg>SEND EMAIL</button>
    </div>
    <div class="chips">
      <span class="chip">CalebMoorePrice23@domain.com <b>✕</b></span>
      <span class="chip">@domain.com <b>✕</b></span>
      <span class="chip">(555) 010-4477 <b>✕</b></span>
      <span class="chip">Seattle <b>✕</b></span>
      <span class="chip">WA <b>✕</b></span>
      <span class="chip">98106 <b>✕</b></span>
      <span class="chip">No Connection <b>✕</b></span>
      <span class="chip">Harbor Mutual <b>✕</b></span>
      <span class="chip">High School Education <b>✕</b></span>
      <span class="chip">1988-2018 <b>✕</b></span>
      <span class="chip">01/01/1988 <b>✕</b></span>
    </div>
  </section>

  <section class="results">
    <div class="results-head">
      <h2>Search Results</h2>
      <div class="filterinput"><svg width="13" height="13" viewBox="0 0 13 13"><circle cx="5.5" cy="5.5" r="4.5" stroke="#777" stroke-width="1.5" fill="none"/><path d="M9 9l3.5 3.5" stroke="#777" stroke-width="1.5"/></svg>Search...</div>
      <div class="tooltip">Tooltip</div>
      <div class="gear"><svg width="16" height="16" viewBox="0 0 16 16"><circle cx="8" cy="8" r="5" fill="none" stroke="#fff" stroke-width="3" stroke-dasharray="2.2 1.7"/><circle cx="8" cy="8" r="3.2" fill="none" stroke="#fff" stroke-width="2"/></svg></div>
      <div class="excel"><svg width="11" height="13" viewBox="0 0 11 13"><path d="M0 0h7l4 4v9H0z" fill="#cc0000"/></svg>EXCEL</div>
    </div>
    <div class="tablebox">
      <table>
        <thead><tr>
          <th class="c-check"><span class="box"></span></th><th class="c-star"></th>
          <th class="c-name">NAME<span class="sort">︿</span></th><th class="c-office">OFFICE<span class="sort">︿</span></th><th class="c-login">LOGIN ID<span class="sort">︿</span></th>
          <th class="c-email">PRIMARY EMAIL<span class="sort">︿</span></th><th class="c-phone">PRIMARY PHONE<span class="sort">︿</span></th><th></th>
        </tr></thead>
        <tbody>
<tr><td class="c-check"><span class="box"></span></td><td class="c-star">☆</td><td>Dalton Reeve</td><td>Orvanta</td><td>- -</td><td>daltonreeve@orvanta.com</td><td>+1 (555) 010-2184</td><td><span class="action">➤ ACTIONS</span></td></tr>
<tr><td class="c-check"><span class="box"></span></td><td class="c-star">☆</td><td>Rosalind Teague</td><td>Tellmark</td><td>- -</td><td>rosalindteague@tellmark.com</td><td>+1 (555) 010-3372</td><td><span class="action">➤ ACTIONS</span></td></tr>
<tr><td class="c-check"><span class="box"></span></td><td class="c-star">☆</td><td>Ione Marsh</td><td>Brevix</td><td>imarsh</td><td>ionemarsh@brevix.com</td><td>+1 (555) 010-4419</td><td><span class="action">➤ ACTIONS</span></td></tr>
<tr><td class="c-check"><span class="box"></span></td><td class="c-star">☆</td><td>Noreen Pak</td><td>Quorlan</td><td>- -</td><td>noreenpak@quorlan.com</td><td>+1 (555) 010-5503</td><td><span class="action">➤ ACTIONS</span></td></tr>
<tr><td class="c-check"><span class="box"></span></td><td class="c-star">☆</td><td>Tamsin Ortega</td><td>Fennic</td><td>- -</td><td>tamsinortega@fennic.com</td><td>+1 (555) 010-6688</td><td><span class="action">➤ ACTIONS</span></td></tr>
<tr><td class="c-check"><span class="box"></span></td><td class="c-star">☆</td><td>Corinne Vale</td><td>Plumline</td><td>- -</td><td>corinnevale@plumline.com</td><td>+1 (555) 010-7291</td><td><span class="action">➤ ACTIONS</span></td></tr>
<tr><td class="c-check"><span class="box"></span></td><td class="c-star">☆</td><td>Maren Holt</td><td>Ventrosa</td><td>- -</td><td>marenholt@ventrosa.com</td><td>+1 (555) 010-8840</td><td><span class="action">➤ ACTIONS</span></td></tr>
<tr><td class="c-check"><span class="box"></span></td><td class="c-star">☆</td><td>Gideon Ashby</td><td>Kelmore</td><td>- -</td><td>gideonashby@kelmore.com</td><td>+1 (555) 010-9157</td><td><span class="action">➤ ACTIONS</span></td></tr>
<tr><td class="c-check"><span class="box"></span></td><td class="c-star">☆</td><td>Priya Dorsey</td><td>Tessaly</td><td>- -</td><td>priyadorsey@tessaly.com</td><td>+1 (555) 010-1263</td><td><span class="action">➤ ACTIONS</span></td></tr>
<tr><td class="c-check"><span class="box"></span></td><td class="c-star">☆</td><td>Odette Lyle</td><td>Stromic</td><td>- -</td><td>odettelyle@stromic.com</td><td>+1 (555) 010-3905</td><td><span class="action">➤ ACTIONS</span></td></tr>
<tr class="selected"><td class="c-check"><span class="box on"><svg width="10" height="8" viewBox="0 0 10 8"><path d="M1 4l3 3 5-6" stroke="#fff" stroke-width="2" fill="none"/></svg></span></td><td class="c-star">★</td><td>Dalton Reeve</td><td>Orvanta</td><td>- -</td><td>daltonreeve@orvanta.com</td><td>+1 (555) 010-2184</td><td><span class="action">➤ ACTIONS</span></td></tr>
<tr class="selected"><td class="c-check"><span class="box on"><svg width="10" height="8" viewBox="0 0 10 8"><path d="M1 4l3 3 5-6" stroke="#fff" stroke-width="2" fill="none"/></svg></span></td><td class="c-star">★</td><td>Rosalind Teague</td><td>Tellmark</td><td>- -</td><td>rosalindteague@tellmark.com</td><td>+1 (555) 010-3372</td><td><span class="action">➤ ACTIONS</span></td></tr>
<tr><td class="c-check"><span class="box"></span></td><td class="c-star">☆</td><td>Ione Marsh</td><td>Brevix</td><td>imarsh</td><td>ionemarsh@brevix.com</td><td>+1 (555) 010-4419</td><td><span class="action">➤ ACTIONS</span></td></tr>
<tr><td class="c-check"><span class="box"></span></td><td class="c-star">☆</td><td>Noreen Pak</td><td>Quorlan</td><td>- -</td><td>noreenpak@quorlan.com</td><td>+1 (555) 010-5503</td><td><span class="action">➤ ACTIONS</span></td></tr>
<tr><td class="c-check"><span class="box"></span></td><td class="c-star">☆</td><td>Tamsin Ortega</td><td>Fennic</td><td>- -</td><td>tamsinortega@fennic.com</td><td>+1 (555) 010-6688</td><td><span class="action">➤ ACTIONS</span></td></tr>
<tr><td class="c-check"><span class="box"></span></td><td class="c-star">☆</td><td>Corinne Vale</td><td>Plumline</td><td>- -</td><td>corinnevale@plumline.com</td><td>+1 (555) 010-7291</td><td><span class="action">➤ ACTIONS</span></td></tr>
<tr><td class="c-check"><span class="box"></span></td><td class="c-star">☆</td><td>Maren Holt</td><td>Ventrosa</td><td>- -</td><td>marenholt@ventrosa.com</td><td>+1 (555) 010-8840</td><td><span class="action">➤ ACTIONS</span></td></tr>
<tr><td class="c-check"><span class="box"></span></td><td class="c-star">☆</td><td>Gideon Ashby</td><td>Kelmore</td><td>- -</td><td>gideonashby@kelmore.com</td><td>+1 (555) 010-9157</td><td><span class="action">➤ ACTIONS</span></td></tr>
        </tbody>
      </table>
      <div class="pager">
        <span class="count"><b>1 - 25</b> of <b>500</b> people</span>
        <div class="pages"><span class="first">&lt;</span><span class="cur">1</span><span>2</span><span>3</span><span>&gt;</span></div>
      </div>
    </div>
  </section>
</div>
</body>
</html>
```